Copper Heron Website

We need a website for our software / project management services company based in South Africa called "Copper Heron". We provide professional services to high value clients in the public and private sectors.

The website must present a highly professional company that exudes quality and confidence.

The theme should be a highly professional subdued look with a fairly limited palette. The neutral tone should be slightly offset with the colours from the company logo. The website should not look dead though, and subtle colour highligting should provide a fresh vibrant feel.

Refer to the current website for general content (www.copperheron.co.za) that may be used. We would also like to make use of social integration and MapLayer.
Updates

Thanks to all the designers that have participated so far and to those that are cooking something up at this very minute :-)

We have received a lot of designs with elements that we absolutely love. So now the hard work of refining these designs can begin.

We'll try and provide feedback on every design received so far ... and await the beautiful designs that we haven't received yet :-)

Good Luck!

Project Deadline Extended
Reason: After careful consideration we are extending the deadline to make small revisions to some of the designs and to select the top three designs. Thank you for everyone who has made a contribution so far - we have several designs that we like and selecting the best one is proving to be difficult :-)

Target Market(s)

The company deals mostly with other businesses, so mostly B2B.

Industry/Entity Type

Software

Requirements
Nice to have
• Social integration

```html
<!DOCTYPE html>
<html lang="en">
<head>
<meta charset="utf-8">
<title>Copper Heron</title>
<link href="https://fonts.googleapis.com/css2?family=Arimo:ital,wght@0,400;0,700;1,700&family=Oswald:wght@500&display=swap" rel="stylesheet">
<style>
  :root {
    --canvas: #e3e3e3;
    --accent-green: #8cc63f;
    --accent-green-dark: #6fa82a;
    --page: #ffffff;
    --ink: #555555;
    --ink-soft: #9a9a9a;
    --logo-grey: #6a6a6a;
    --banner-top: #4aa6c9;
    --banner-bottom: #2f8cb2;
    --card-top: #3a8fa2;
    --card-bottom: #226f82;
    --button-top: #29b7d6;
    --button-bottom: #0f8aa9;
  }
  * { box-sizing: border-box; margin: 0; padding: 0; }
  html, body { width: 1200px; height: 1200px; overflow: hidden; }
  body {
    position: relative;
    background: var(--canvas);
    font-family: "Arimo", Arial, sans-serif;
    color: var(--ink);
  }
  .edge { position: absolute; left: 0; width: 1200px; height: 6px; background: var(--accent-green); }
  .edge--top { top: 0; }
  .edge--bottom { bottom: 0; }

  .page {
    position: absolute; left: 120px; top: 6px; width: 960px; height: 1188px;
    background: radial-gradient(ellipse at 50% 45%, #ffffff 60%, #f1f1f1 100%);
  }

  .brand {
    position: absolute; left: 340px; top: 88px; width: 300px;
    font-family: "Oswald", "Arial Narrow", sans-serif; font-weight: 500;
    font-size: 56px; line-height: 70px; color: var(--logo-grey); letter-spacing: -0.5px;
    display: flex; align-items: center; gap: 14px; white-space: nowrap;
  }
  .brand__dot { width: 26px; height: 26px; border-radius: 50%; background: var(--accent-green); flex: none; }

  .nav {
    position: absolute; left: 10px; top: 185px; width: 940px; height: 46px;
    background: linear-gradient(#ffffff, #f0f0f0 60%, #e2e2e2);
    border: 1px solid #d4d4d4; border-radius: 4px;
    box-shadow: 0 10px 12px -10px rgba(0,0,0,0.35);
  }
  .nav__item {
    position: absolute; top: 0; height: 44px; line-height: 44px;
    font-size: 12px; font-weight: 700; color: #333; text-transform: uppercase;
  }
  .nav__item--home { left: 25px; }
  .nav__divider { position: absolute; left: 78px; top: 6px; width: 1px; height: 34px; background: #cfcfcf; }
  .nav__item--company { left: 108px; }
  .nav__item--active {
    left: 200px; width: 187px; text-align: center; font-weight: 400; color: #555;
    background: linear-gradient(#e6e6e6, #d0d0d0);
  }
  .nav__item--portfolio { left: 418px; }
  .nav__item--contact { left: 530px; }
  .social { position: absolute; left: 807px; top: 5px; display: flex; gap: 8px; }
  .social__tile {
    width: 34px; height: 34px; border-radius: 6px;
    background: linear-gradient(#5ea9d9, #2f7fb4); box-shadow: 0 1px 2px rgba(0,0,0,0.3);
  }
  .social__tile:nth-child(2) { background: linear-gradient(#7cc7df, #3f9bbd); }
  .social__tile:nth-child(3) { background: linear-gradient(#5a82c6, #2f55a0); }

  .submenu {
    position: absolute; left: 211px; top: 232px; width: 187px; z-index: 5;
    background: var(--accent-green); list-style: none;
    box-shadow: 0 2px 4px rgba(0,0,0,0.2);
  }
  .submenu li {
    height: 22px; line-height: 22px; padding-left: 12px;
    font-size: 14px; color: #fff; border-bottom: 1px solid #a6d66a;
  }
  .submenu li:last-child { border-bottom: none; color: #333; }

  .intro {
    position: absolute; left: 10px; top: 262px; width: 940px; height: 483px;
    background: var(--page); border: 1px solid #dcdcdc; border-radius: 4px;
    box-shadow: 0 14px 12px -12px rgba(0,0,0,0.4);
  }
  .banner {
    position: absolute; left: 0; top: 33px; width: 938px; height: 117px;
    background: linear-gradient(var(--banner-top), var(--banner-bottom));
  }
  .banner__title {
    position: absolute; left: 24px; top: 14px;
    font-weight: 700; font-size: 35px; line-height: 40px; color: #fff; letter-spacing: 0.5px;
    white-space: nowrap;
  }
  .banner__visual {
    position: absolute; right: 10px; top: 0; width: 260px; height: 117px;
    background: radial-gradient(ellipse at 60% 45%, #9fdcf0 0%, #5fb7d6 45%, rgba(47,140,178,0) 80%);
  }
  .intro__lead {
    position: absolute; left: 24px; top: 166px; width: 800px;
    font-weight: 700; font-style: italic; font-size: 19px; line-height: 25px; color: #8a8a8a;
  }
  .intro__copy {
    position: absolute; left: 24px; width: 880px;
    font-size: 14.5px; line-height: 19.5px; color: var(--ink-soft);
  }
  .intro__copy--one { top: 243px; }
  .intro__copy--two { top: 358px; }

  .card {
    position: absolute; top: 777px; width: 300px; height: 248px;
    background: linear-gradient(var(--card-top), var(--card-bottom));
    border-radius: 4px; color: #fff;
    box-shadow: 0 2px 4px rgba(0,0,0,0.25);
  }
  .card--one { left: 10px; }
  .card--two { left: 330px; }
  .card--map { left: 650px; }
  .card__title {
    position: absolute; left: 24px; top: 22px; display: flex; align-items: center; gap: 10px;
    font-weight: 700; font-style: italic; font-size: 21px; letter-spacing: 0.5px;
  }
  .card__text {
    position: absolute; left: 22px; top: 64px; width: 262px;
    font-size: 13px; line-height: 16.6px; color: #e4f2f6;
  }
  .card__more { position: absolute; right: 18px; top: 218px; font-size: 13px; color: #d7ecf2; }
  .card--map .card__title { left: 47px; }
  .map {
    position: absolute; left: 8px; top: 60px; width: 285px; height: 114px;
    background: linear-gradient(135deg, #e9e9e6, #d3d6d2 55%, #c9cdc8);
    border: 2px solid #ffffff;
  }
  .map-button {
    position: absolute; left: 45px; top: 185px; width: 213px; height: 36px;
    background: linear-gradient(var(--button-top), var(--button-bottom));
    border-radius: 4px; text-align: center; line-height: 36px;
    font-weight: 700; font-size: 17px; letter-spacing: 1px; color: #fff;
    box-shadow: 0 3px 4px rgba(0,0,0,0.3);
  }
  .map-credit {
    position: absolute; left: 0; width: 300px; top: 229px; text-align: center;
    font-size: 11px; color: var(--accent-green);
  }

  .footer-nav {
    position: absolute; left: 0; width: 960px; top: 1038px; text-align: center;
    font-size: 12.5px; font-weight: 700; color: #444; word-spacing: 2px;
  }
  .footer-nav span { color: #777; margin: 0 6px; }
</style>
</head>
<body>
  <div class="edge edge--top"></div>
  <div class="edge edge--bottom"></div>

  <div class="page">
    <div class="brand"><span class="brand__dot"></span>Copper Heron</div>

    <nav class="nav">
      <span class="nav__item nav__item--home">Home</span>
      <span class="nav__divider"></span>
      <span class="nav__item nav__item--company">Company</span>
      <span class="nav__item nav__item--active">Professional Services</span>
      <span class="nav__item nav__item--portfolio">Portfolio</span>
      <span class="nav__item nav__item--contact">Contact Us</span>
      <div class="social" aria-label="Social links">
        <span class="social__tile"></span>
        <span class="social__tile"></span>
        <span class="social__tile"></span>
      </div>
    </nav>

    <ul class="submenu">
      <li>Lorem ipsum dolor sit</li>
      <li>Lorem ipsum dolor sit</li>
      <li>Lorem ipsum dolor sit</li>
      <li>Lorem ipsum dolor sit</li>
      <li>Lorem ipsum dolor sit</li>
      <li>Lorem ipsum dolor sit</li>
      <li>Lorem ipsum dolor sit</li>
    </ul>

    <section class="intro">
      <div class="banner">
        <h1 class="banner__title">Copper Heron<br>a premium software solutions provider</h1>
        <div class="banner__visual" role="img" aria-label="Hand touching floating digital screens"></div>
      </div>
      <p class="intro__lead">which delivers quality software development support services to clients in all sectors of industry.</p>
      <p class="intro__copy intro__copy--one">Our value proposition builds on customers' needs to successfully implement software development projects within a given set of time, quality and budgetary constraints. Our focus is to provide customers with a full set of products and services to support each phase of the software development lifecycle whilst offering the benefits of flexibility in scaling of resources, cost reduction, improved cost management, access to specialized skills and the ability to focus on strategic business needs.</p>
      <p class="intro__copy intro__copy--two">Our absolute obsession with delivering quality software artifacts on time and in budget is what differentiates us from our competitors. We are able to live out this passion by partnering with our clients to ensure that the correct people, processes and technology are applied to each software development project.</p>
    </section>

    <article class="card card--one">
      <h2 class="card__title">
        <svg width="26" height="26" viewBox="0 0 24 24" aria-hidden="true"><path d="M12 2l2.9 6.6 7.1.6-5.4 4.7 1.6 7-6.2-3.8-6.2 3.8 1.6-7L2 9.2l7.1-.6z" fill="#7fa3ad"/></svg>
        Lorem ipsum dolor
      </h2>
      <p class="card__text">Lorem ipsum dolor sit amet, consectetuer adipiscing elit, sed diam nonummy nibh euismod tincidunt ut laoreet dolore magna aliquam erat volutpat. Ut wisi enim ad minim veniam, quis nostrud exerci tation ullamcorper suscipit lobortis nisl ut aliquip ex ea commodo consequat.</p>
      <span class="card__more">read more &gt;&gt;</span>
    </article>

    <article class="card card--two">
      <h2 class="card__title">
        <svg width="26" height="26" viewBox="0 0 24 24" aria-hidden="true"><path d="M12 2l2.9 6.6 7.1.6-5.4 4.7 1.6 7-6.2-3.8-6.2 3.8 1.6-7L2 9.2l7.1-.6z" fill="#7fa3ad"/></svg>
        Lorem ipsum dolor
      </h2>
      <p class="card__text">Lorem ipsum dolor sit amet, consectetuer adipiscing elit, sed diam nonummy nibh euismod tincidunt ut laoreet dolore magna aliquam erat volutpat. Ut wisi enim ad minim veniam, quis nostrud exerci tation ullamcorper suscipit lobortis nisl ut aliquip ex ea commodo consequat.</p>
      <span class="card__more">read more &gt;&gt;</span>
    </article>

    <article class="card card--map">
      <h2 class="card__title">Check our location</h2>
      <div class="map" role="img" aria-label="Street map showing the office location"></div>
      <div class="map-button">CLICK HERE</div>
      <div class="map-credit">Powered by MapLayer</div>
    </article>

    <nav class="footer-nav">Home<span>|</span>Company<span>|</span>Professional services<span>|</span>Portfolio<span>|</span>Contact us</nav>
  </div>
</body>
</html>
```